High end boutique food product label

We are looking for a label design to be used on our range of high end food products. We don't have a design or colour scheme in mind and are interested to see what ideas are submitted.
We would like it to feel sophisticated, chic, and eye-catching.
All of our products are handmade in Australia using Australian ingredients.
The graphics for the label will need to be scaleable to be fit a variety of labels from small squat jars with labels sized 3.5cm high and 7cm wide, to tall thin bottles with labels that are 14cm high and 4.5cm wide.
We would be interested in working with the winning designer to create these different sized labels.
The label submitted for this project should be 14cm high and 4.5cm wide, it should include our logo (file supplied in .jpeg and .ai), the product name 'Extra Virgin Olive Oil' and the size '250ml'.
This is just the front label on a bottle, we are not expecting a rear label to be created currently.
You are welcome to use any fonts you think will look good but the fonts used in our logo are Allaina Medium and Bebas Kai Regular.

```html
<!DOCTYPE html>
<html lang="en">
<head>
<meta charset="utf-8">
<title>Harlow Pantry – Extra Virgin Olive Oil Labels</title>
<link rel="stylesheet" href="https://fonts.googleapis.com/css2?family=Bebas+Neue&display=swap">
<style>
  :root {
    --page: #ffffff;
    --kraft: #c1a983;
    --espresso: #43291a;
    --ink: #4a2e1e;
    --cream: #f6efe3;
    --sprig-a: #b0946c;
    --sprig-b: #9c7f58;
  }
  * { box-sizing: border-box; margin: 0; padding: 0; }
  html, body {
    width: 1200px; height: 927px; overflow: hidden;
    background: var(--page);
    font-family: "Bebas Neue", "Arial Narrow", sans-serif;
  }
  .label-sheet {
    position: relative; width: 1200px; height: 927px;
    display: flex; justify-content: center; align-items: center; gap: 60px;
  }
  .label {
    position: relative; width: 260px; height: 810px;
    background: var(--kraft); color: var(--ink);
  }
  .label__shapes { position: absolute; inset: 0; }
  .label__text {
    position: absolute; left: 0; width: 100%;
    text-align: center; line-height: 1; letter-spacing: 0.5px;
  }
  .brand-name {
    color: var(--cream); font-size: 34px; letter-spacing: 1px;
  }
  .product-name { font-size: 37px; }
  .product-name--lead { font-size: 41px; }
  .product-name--hero { font-size: 56px; }
  .origin-note { font-size: 16px; letter-spacing: 0.6px; }
  .volume { font-size: 38px; }
  .olive-sprig {
    position: absolute; border-radius: 40% 55% 45% 50%;
    background: radial-gradient(ellipse at 45% 45%, var(--sprig-b), var(--sprig-a) 70%, var(--kraft));
  }
</style>
</head>
<body>
<main class="label-sheet">

  <!-- Variant one: inset header, name below -->
  <section class="label label--inset">
    <svg class="label__shapes" width="260" height="810" viewBox="0 0 260 810">
      <rect x="19" y="19" width="222" height="772" fill="none" stroke="var(--espresso)" stroke-width="1.6"/>
      <path d="M19 19 H241 V175 Q130 275 19 175 Z" fill="var(--espresso)"/>
    </svg>
    <p class="label__text brand-name" style="top:122px;">Harlow Pantry</p>
    <div class="olive-sprig" role="img" aria-label="Hand-drawn olive branch with fruit and leaves" style="left:43px; top:309px; width:175px; height:183px;"></div>
    <p class="label__text product-name" style="top:572px;">Extra Virgin</p>
    <p class="label__text product-name" style="top:612px;">Olive Oil</p>
    <p class="label__text origin-note" style="top:662px;">100% Australian Made</p>
    <p class="label__text volume" style="top:716px;">250ML</p>
  </section>

  <!-- Variant two: full-bleed header, name on top -->
  <section class="label label--bleed">
    <svg class="label__shapes" width="260" height="810" viewBox="0 0 260 810">
      <path d="M0 0 H260 V169 Q130 278 0 169 Z" fill="var(--espresso)"/>
      <path d="M21 212 Q130 270 240 212 V787 H21 Z" fill="none" stroke="var(--espresso)" stroke-width="1.6"/>
      <line x1="30" y1="404" x2="231" y2="404" stroke="var(--espresso)" stroke-width="1.4"/>
    </svg>
    <p class="label__text brand-name" style="top:122px;">Harlow Pantry</p>
    <p class="label__text product-name product-name--lead" style="top:276px;">Extra Virgin</p>
    <p class="label__text product-name product-name--hero" style="top:312px;">Olive Oil</p>
    <p class="label__text origin-note" style="top:373px;">100% Australian Made</p>
    <div class="olive-sprig" role="img" aria-label="Hand-drawn olive branch with fruit and leaves" style="left:45px; top:460px; width:171px; height:182px;"></div>
    <p class="label__text volume" style="top:714px;">250ML</p>
  </section>

</main>
</body>
</html>
```